New Business Card Design for Business Consulting Business

We need a business card design that reflects the simplicity of our business. We partner with our clients to help them deliver change. We are a different kind of business consulting group. We don't just provide you with the theory. We provide you with the leadership and capability to execute change.

Vonduro is a professional services organisation that partners with their clients to lead the execution of strategic process and system improvement initiatives. Vonduro combines hands on delivery with coaching in best practice methodologies and approaches to build their clients capabilities to ensure their ongoing success in project implementations. Vonduro offers business advisory services in Project Management, Business Process Management, Change Management and Business Analytics.

Reason: Hi Designers, Thanks for all of your great designs. There are some really creative and cool ideas. Everyone is really capturing the essence of my business Vonduro. I am extending the deadline for the business card design by 6 days as I need to consult my Marketing colleague who won't be back in Australia until Wednesday. I would like to sit down with them and review all of the best designs. The key themes of the things I have really liked on my first review are: 1) Capturing the company website on the back of the card. 2) Including the company logo on the back of the card too. 3) Including the types of services on the back of the card that the company offers - Project Management - Business Process Management - Change Management - Business Analytics 4) Utilising some images on the back of the card Just so everyone knows the colour palette for the Vonduro company logo is: R: 0 G: 86 B: 162 or C: 97% M: 73% Y: 4% K: 0% Thanks Gareth

Hi Designers,

Thanks for all of your submissions to date.  I am working through each design and will provide feedback on all the great work.

One thing I would like to ask is if you could submit a version that has my academic credentials under or after my name.  I am not a big fan of doing this but as I am in business consulting it does seem to be quite common.

I hold a Bachelor of Commerce (BCom) and a Master of Business Administration (MBA)

Thanks

Gareth

Hi Designers,

Thanks for all of your fantastic designs.  There are some really great designs here for my business.  I am still in the process of reviewing designs and should have this completed by tomorrow.  Some of the things I have learnt from this round of designs are:

1) I prefer to have the card without my academic qualifications

2) I really like cards that have a blue back

3) I prefer to have my name and title either left or right of centre

I hope this helps and I will endeavour to get through all of the designs tomorrow

Cheers

Gareth

Target Market(s)

We target large corporate organisations

Industry/Entity Type

Leadership

Requirements
Must have
• Must have the following business details

Gareth Pilling - Director
Address: Level 7, 82 Harlow Street, Melbourne, Australia, 3000
Phone: +61 3 527 840 213
Fax: +61 3 9214 5037
Email: gareth.pilling@vonduro-example.com.au
LinkedIn: au.linkedin.com/in/garethjpilling/
Twiiter: @garethjpilling
Website: www.vonduro-example.com.au

```html
<!DOCTYPE html>
<html lang="en">
<head>
<meta charset="utf-8">
<title>Vonduro Business Card</title>
<link rel="stylesheet" href="https://fonts.googleapis.com/css2?family=Mulish:wght@400;800&display=swap">
<style>
  :root {
    --backdrop: #2e2f31;
    --brand-blue: #3e5c9a;
    --card-white: #ffffff;
    --ink-blue: #3e5c9a;
  }
  * { margin: 0; padding: 0; box-sizing: border-box; }
  html, body { width: 1200px; height: 807px; overflow: hidden; }
  body {
    background: var(--backdrop);
    font-family: "Mulish", Arial, sans-serif;
    position: relative;
  }
  .card {
    position: absolute;
    top: 249px;
    width: 540px;
    height: 309px;
  }
  .card-back { left: 50px; background: var(--brand-blue); }
  .card-front { left: 610px; background: var(--card-white); color: var(--ink-blue); }

  .wordmark { position: absolute; }
  .wordmark-name { display: block; font-weight: 400; line-height: 1; white-space: nowrap; }
  .wordmark-suffix { display: block; text-align: right; font-weight: 400; line-height: 1; }

  .card-back .wordmark { left: 70px; top: 102px; color: var(--card-white); }
  .card-back .wordmark-name { font-size: 76px; letter-spacing: 1px; }
  .card-back .wordmark-suffix { font-size: 13px; margin-top: 8px; }

  .card-front .wordmark { left: 34px; top: 32px; color: var(--ink-blue); }
  .card-front .wordmark-name { font-size: 30px; }
  .card-front .wordmark-suffix { font-size: 7px; margin-top: 4px; }

  .identity {
    position: absolute;
    right: 305px;
    top: 132px;
    text-align: right;
    white-space: nowrap;
  }
  .identity-name { font-weight: 800; font-size: 21px; text-transform: uppercase; letter-spacing: 0.2px; }
  .identity-title { font-weight: 400; font-size: 20px; margin-top: 2px; }

  .divider {
    position: absolute;
    left: 247px;
    top: 132px;
    width: 1px;
    height: 128px;
    background: var(--ink-blue);
  }
  .contact-list {
    position: absolute;
    left: 258px;
    top: 132px;
    list-style: none;
    font-size: 11px;
    line-height: 18px;
    white-space: nowrap;
  }
</style>
</head>
<body>
  <section class="card card-back" aria-label="Card back">
    <div class="wordmark">
      <span class="wordmark-name">Vonduro</span>
      <span class="wordmark-suffix">Pty Ltd</span>
    </div>
  </section>

  <section class="card card-front" aria-label="Card front">
    <div class="wordmark">
      <span class="wordmark-name">Vonduro</span>
      <span class="wordmark-suffix">Pty Ltd</span>
    </div>

    <div class="identity">
      <p class="identity-name">Gareth Pilling</p>
      <p class="identity-title">Director</p>
    </div>

    <div class="divider" aria-hidden="true"></div>

    <ul class="contact-list">
      <li>A: Level 7, 82 Harlow Street, Melbourne 3000</li>
      <li>P: +61 3 527 840 213</li>
      <li>F: +61 3 9214 5037</li>
      <li>E: gareth.pilling@vonduro-example.com.au</li>
      <li>LinkedIn: au.linkedin.com/in/garethjpilling/</li>
      <li>Twitter: @garethjpilling</li>
      <li>Website: www.vonduro-example.com.au</li>
    </ul>
  </section>
</body>
</html>
```